Awesome Business Card Design needed!

Hey there.
I'm looking for a simple but awesome business card design.
Type of company: Online advertisement agency
(please don't use the typical business people or statistics images on the card)
The front has to display the business name
and possibly some sort of logo ( perhaps something with the two M's of the biz name )
And the back of the card should say:
Name
Phone
Email
Let your imagination flow.
here are some designs that I like and that you can use as inspiration.
Simple but Awesome
http://images.pixelvantor.net/designs/55128_877673_43091_thumbnail.jpg
http://images.pixelvantor.net/designs/37714_747642_40106_image.jpg
http://images.pixelvantor.net/designs/55128_877673_43091_image.jpg
http://images.pixelvantor.net/designs/51321_781878_43091_image.jpg
http://images.pixelvantor.net/designs/33378_399063_15912_image.jpg
http://images.pixelvantor.net/designs/2337_271604_9495_image.jpg
good luck

```html
<!DOCTYPE html>
<html lang="en">
<head>
<meta charset="utf-8">
<title>Velora Media – Business Card</title>
<link href="https://fonts.googleapis.com/css2?family=Raleway:wght@300&family=Open+Sans:wght@400&display=swap" rel="stylesheet">
<style>
  :root {
    --page-bg: #eceeef;
    --front-bg: #0b0909;
    --front-swoosh: #1c1616;
    --gold: #c89b5a;
    --gold-light: #e3c08d;
    --gold-dark: #8e6636;
    --bar-tip: #f3ece6;
    --back-teal: #5aa9bf;
    --back-blue: #3fb2db;
    --back-cream: #f4ecc2;
    --ink: #121212;
    --ink-soft: #2a2a2a;
    --mark-fill: #0a0a0a;
    --mark-ring: #4db3cf;
  }
  * { margin: 0; padding: 0; box-sizing: border-box; }
  html, body {
    width: 1200px; height: 621px; overflow: hidden;
    background: var(--page-bg);
  }
  .stage { position: relative; width: 1200px; height: 621px; }

  .card {
    position: absolute; top: 268px;
    width: 487px; height: 282px;
    border-radius: 30px; overflow: hidden;
  }

  /* Front */
  .card--front { left: 77px; background: var(--front-bg); }
  .card--front .swooshes { position: absolute; inset: 0; }
  .accent-bar {
    position: absolute; left: 0; top: 130px;
    width: 62px; height: 22px;
    background: linear-gradient(90deg, var(--gold-dark), var(--gold-light) 70%, var(--gold));
  }
  .accent-tip {
    position: absolute; left: 65px; top: 130px;
    width: 16px; height: 22px; background: var(--bar-tip);
  }
  .front-wordmark {
    position: absolute; left: 86px; top: 125px;
    font-family: "Raleway", sans-serif; font-weight: 300;
    font-size: 27px; letter-spacing: 3px; line-height: 32px;
    color: var(--gold); white-space: nowrap;
  }
  .front-ring {
    position: absolute; left: 387px; top: 92px;
    width: 84px; height: 84px; border-radius: 50%;
    border: 2px solid var(--gold);
  }

  /* Back */
  .card--back {
    left: 641px;
    background:
      radial-gradient(ellipse 60% 70% at 30% 110%, var(--back-blue) 0%, rgba(63,178,219,0) 70%),
      linear-gradient(100deg, var(--back-teal) 0%, #8cc8d6 45%, #d7e7d6 70%, var(--back-cream) 100%);
  }
  .back-disc {
    position: absolute; left: 26px; top: 15px;
    width: 114px; height: 114px; border-radius: 50%;
    background: var(--mark-fill);
  }
  .back-wordmark {
    position: absolute; left: 148px; top: 55px;
    font-family: "Raleway", sans-serif; font-weight: 300;
    font-size: 30px; letter-spacing: 4px; line-height: 36px;
    color: var(--ink); white-space: nowrap;
  }
  .contact-list {
    position: absolute; left: 58px; top: 170px;
    list-style: none;
    font-family: "Open Sans", sans-serif; font-size: 16px;
    color: var(--ink); letter-spacing: 1px;
  }
  .contact-row { display: flex; align-items: center; height: 31px; }
  .contact-label { width: 62px; font-size: 15px; color: var(--ink-soft); }
  .contact-icon { width: 62px; display: flex; align-items: center; padding-left: 6px; }
  .contact-icon svg { display: block; }
</style>
</head>
<body>
<main class="stage">

  <section class="card card--front" aria-label="Card front">
    <svg class="swooshes" width="487" height="282" viewBox="0 0 487 282" aria-hidden="true">
      <path d="M0 105 C120 70 300 60 487 90 L487 0 L0 0 Z" fill="var(--front-swoosh)" opacity="0.55"/>
      <path d="M0 200 C150 170 330 175 487 150 L487 282 L0 282 Z" fill="var(--front-swoosh)" opacity="0.45"/>
      <path d="M380 0 C430 20 470 40 487 60 L487 0 Z" fill="#2a2020"/>
    </svg>
    <div class="accent-bar"></div>
    <div class="accent-tip"></div>
    <p class="front-wordmark">VELORA &nbsp;Media</p>
    <div class="front-ring"></div>
  </section>

  <section class="card card--back" aria-label="Card back">
    <div class="back-disc"></div>
    <p class="back-wordmark">VELORA Media</p>
    <ul class="contact-list">
      <li class="contact-row">
        <span class="contact-label">name</span>
        <span class="contact-value">Velora Media</span>
      </li>
      <li class="contact-row">
        <span class="contact-icon" aria-label="Phone">
          <svg width="26" height="14" viewBox="0 0 26 14">
            <path d="M1 6 C6 0 20 0 25 6 L25 10 L19 10 L19 6 C15 4 11 4 7 6 L7 10 L1 10 Z" fill="var(--ink)"/>
            <rect x="9" y="8" width="8" height="5" rx="1" fill="var(--ink)"/>
          </svg>
        </span>
        <span class="contact-value">(055) 412 738</span>
      </li>
      <li class="contact-row">
        <span class="contact-icon" aria-label="Email">
          <svg width="28" height="26" viewBox="0 0 28 26">
            <path d="M2 10 L14 2 L26 10 L26 24 L2 24 Z" fill="none" stroke="var(--ink)" stroke-width="1.6" stroke-linejoin="round"/>
            <path d="M2 10 L14 18 L26 10" fill="none" stroke="var(--ink)" stroke-width="1.6" stroke-linejoin="round"/>
          </svg>
        </span>
        <span class="contact-value">hello@veloramedia.net</span>
      </li>
    </ul>
  </section>

</main>
</body>
</html>
```